Marwell Herd Services concrete grooving services flyer design

Marwell Herd Services offers 4 different grooving options:

DEEP GROOVING
, ideal for Safety & Efficiency
Our hugely popular deep straight line grooving, long lasting, minimal hoof wear,

Create safe and secure flooring, cows walk without hesitation

Achieve groove spacing for optimal hoof function, reduce hoof trauma

Ideal grooves to new concrete or surfaces with little to no pattern or previous grooving

Ideal groove pattern as promoted by The pasturewide programme

MINI GROOVING,
Smaller dimensions Ideal option for heifer housing and high activity areas such as parlours and handling areas

An ideal solution for regaining traction on old previous grooving that has lost its traction without loosing stability

Plaining

smoothing down rough concrete with previous aggressive grooving or patterns to reduce hoof trauma & wear

SENSOR PLATE SINKING

sinking sensor plates for automated machines below surface level preventing accidental damage & wear

```html
<!DOCTYPE html>
<html lang="en">
<head>
<meta charset="utf-8">
<title>Marwell Herd Services – Concrete Grooving Flyer</title>
<link href="https://fonts.googleapis.com/css2?family=Oswald:wght@400;500;700&family=Roboto+Condensed:ital,wght@0,400;0,700;1,700&family=Roboto:wght@400;500&display=swap" rel="stylesheet">
<style>
:root{
  --stage:#9b9b9b;
  --green:#0b6a2d;
  --green-dark:#06401b;
  --green-light:#3aa64f;
  --charcoal:#333333;
  --black:#000000;
  --yellow:#ffcc00;
  --text-yellow:#f2c400;
  --white:#ffffff;
  --concrete-light:#e7e4dc;
  --concrete-mid:#b9b3a6;
  --concrete-dark:#7b7367;
}
*{margin:0;padding:0;box-sizing:border-box}
html,body{width:1200px;height:2505px;overflow:hidden;background:var(--stage)}
body{position:relative;font-family:"Roboto Condensed",sans-serif;color:var(--white)}
.abs{position:absolute}
.spread{position:absolute;left:126px;width:950px;height:670px;overflow:hidden;box-shadow:0 6px 14px rgba(0,0,0,.35)}
.spread-outside{top:120px;background:var(--green)}
.spread-inside{top:875px;background:var(--charcoal)}
.photo{position:absolute}
.concrete{background:linear-gradient(160deg,var(--concrete-light),var(--concrete-mid) 55%,var(--concrete-dark))}
.concrete-warm{background:linear-gradient(170deg,#cfc3ab,#9b8a6d 60%,#5e5240)}
.barn-yellow{background:linear-gradient(160deg,#caa32a,#8a6a12)}
.heading{font-family:"Oswald",sans-serif;font-weight:500;text-transform:uppercase;line-height:1.05;white-space:nowrap}
.sensor-panel{left:0;top:50px;width:280px;height:620px;background:var(--charcoal)}
.sensor-panel h2{position:absolute;left:24px;top:24px;font-size:28px}
.sensor-panel p{position:absolute;left:24px;top:96px;width:190px;font-size:12.5px;line-height:17.5px}
.middle-panel{left:316px;top:0;width:316px;height:670px;background:var(--black)}
.middle-panel h2{position:absolute;left:25px;top:296px;font-size:28px}
.middle-panel .lede{position:absolute;left:25px;top:336px;width:230px;font-size:12.5px;line-height:17.5px}
.contact{position:absolute;left:25px;top:428px;width:233px}
.contact .company{font-family:"Roboto",sans-serif;font-size:20px;margin-top:18px;white-space:nowrap}
.contact .address{font-family:"Roboto",sans-serif;font-size:11.5px;line-height:17px;margin-top:6px;padding-bottom:10px;border-bottom:2px solid var(--green)}
.contact .tel{font-family:"Oswald",sans-serif;font-size:23px;padding:8px 0 6px;border-bottom:2px solid var(--green)}
.contact .web{font-family:"Oswald",sans-serif;font-weight:400;color:var(--text-yellow);font-size:18px;padding:6px 0 6px;border-bottom:2px solid var(--green)}
.contact .email{font-family:"Roboto",sans-serif;font-size:11.5px;margin-top:10px;white-space:nowrap}
.cover{left:632px;top:0;width:318px;height:670px}
.brand{position:absolute;left:37px;top:0;width:122px;height:170px;display:flex;flex-direction:column;align-items:center;justify-content:center;gap:8px}
.brand .mark{width:22px;height:22px;border-radius:50%;background:var(--green)}
.brand .name{font-family:"Oswald",sans-serif;font-weight:500;font-size:18px;color:var(--black);letter-spacing:1px}
.cover h1{position:absolute;left:44px;top:428px;font-family:"Oswald",sans-serif;font-weight:700;font-size:52px;line-height:52px;text-transform:uppercase}
.cover h1 span{font-weight:400;display:block}
.services{position:absolute;left:44px;top:592px;width:270px;display:grid;grid-template-columns:118px 1fr;row-gap:6px;font-family:"Oswald",sans-serif;font-weight:400;font-size:14.5px;color:var(--text-yellow)}
.services li{list-style:none;padding-left:10px;position:relative;white-space:nowrap}
.services li::before{content:"";position:absolute;left:0;top:6px;border-left:6px solid var(--green-light);border-top:4px solid transparent;border-bottom:4px solid transparent}
.band{left:0;top:0;width:950px;height:133px}
.band h2{position:absolute;left:0;top:52px;width:950px;text-align:center;font-family:"Oswald",sans-serif;font-size:42px;font-weight:500;color:#222;white-space:nowrap}
.band h2 .lead{color:var(--green)}
.band h2 .strong{font-weight:700}
.band h2 .light{font-weight:400}
.tagbar{left:0;top:173px;width:86px;height:352px;background:var(--green)}
.tagbar p{position:absolute;left:43px;top:176px;transform:translate(-50%,-50%) rotate(-90deg);white-space:nowrap;font-style:italic;font-weight:700;text-align:center;line-height:24px}
.tagbar .t1{font-size:25px;color:var(--text-yellow)}
.tagbar .t2{font-size:19px;font-weight:400;display:block;font-style:normal;font-family:"Oswald",sans-serif}
.deep{left:399px;top:195px;width:192px}
.deep h3{font-size:27px;margin-bottom:10px}
.deep ul{list-style:none}
.deep li{font-size:12px;line-height:15px;padding:0 0 6px;margin-bottom:7px;border-bottom:1px solid #777}
.deep li:last-child{border-bottom:0;margin-bottom:0}
.deep li em{font-style:normal;color:var(--text-yellow)}
.mini-bg{left:632px;top:133px;width:318px;height:410px}
.mini-green{left:632px;top:543px;width:318px;height:127px;background:var(--green)}
.mini-box{left:664px;top:200px;width:253px;height:460px;background:rgba(0,0,0,.88)}
.mini-box h3{position:absolute;left:24px;top:258px;font-size:29px}
.mini-box .p1{position:absolute;left:24px;top:302px;width:210px;font-size:12.2px;line-height:17.5px}
.mini-box .p2{position:absolute;left:24px;top:370px;width:210px;font-size:12.2px;line-height:17.5px;padding-top:6px;border-top:1px solid #777}
</style>
</head>
<body>

<section class="spread spread-outside" aria-label="Flyer outside spread">
  <div class="abs sensor-panel">
    <h2 class="heading">Sensor<br>Plate Sinking</h2>
    <p>Sinking Sensor Plates For Automated Machines Below Surface Level Preventing Accidental Damage &amp; Wear</p>
  </div>
  <div class="photo concrete-warm" style="left:0;top:220px;width:244px;height:212px" role="img" aria-label="Photo of a sunk sensor plate channel in a concrete floor beside a feeding machine"></div>
  <div class="photo concrete-warm" style="left:0;top:445px;width:244px;height:225px" role="img" aria-label="Close-up photo of grooved concrete around a sunk sensor plate"></div>

  <div class="abs middle-panel">
    <div class="photo concrete" style="left:25px;top:0;width:266px;height:280px" role="img" aria-label="Photo of freshly planed concrete in a cattle shed"></div>
    <h2 class="heading">Plaining</h2>
    <p class="lede">smoothing down rough concrete with previous aggressive grooving or patterns to reduce hoof trauma &amp; wear</p>
    <div class="contact">
      <svg width="150" height="16" viewBox="0 0 150 16" aria-hidden="true"><path d="M2 14 Q70 -4 148 12" fill="none" stroke="var(--green)" stroke-width="4"/></svg>
      <div class="company">Marwell Herd Services Ltd</div>
      <div class="address">4 Brookend Cottage, Harlow Lane, Oakfield,<br>Shropshire. SY99 2ZZ.</div>
      <div class="tel">Tel : 07700 900412</div>
      <div class="web">marwellherdservicesltd.com</div>
      <div class="email">Email :&nbsp; marwellherdservices@example.com</div>
    </div>
  </div>

  <div class="abs cover">
    <svg class="abs" style="left:0;top:0" width="318" height="670" viewBox="0 0 318 670" aria-hidden="true">
      <defs>
        <linearGradient id="coverConcrete" x1="0" y1="0" x2="1" y2="1">
          <stop offset="0" stop-color="#dcd9d2"/><stop offset=".6" stop-color="#a9a59c"/><stop offset="1" stop-color="#6f6a60"/>
        </linearGradient>
      </defs>
      <rect width="318" height="670" fill="var(--green)"/>
      <polygon points="0,0 318,0 318,62 0,210" fill="var(--yellow)"/>
      <polygon points="0,210 318,62 318,380 232,440 0,370" fill="url(#coverConcrete)" role="img" aria-label="Photo of radiating grooves in a cattle shed floor"/>
      <polygon points="0,370 232,440 0,520" fill="var(--black)"/>
      <polygon points="250,430 318,380 318,610 270,640" fill="#2f5a36" opacity=".6"/>
      <polygon points="37,0 159,0 159,142 37,185" fill="var(--white)"/>
    </svg>
    <div class="brand"><span class="mark"></span><span class="name">MARWELL</span></div>
    <h1>Concrete<br>Grooving<span>Services</span></h1>
    <ul class="services">
      <li>Deep Grooving</li><li>Mini Grooving,</li>
      <li>Plaining</li><li>Sensor Plate Sinking</li>
    </ul>
  </div>
</section>

<section class="spread spread-inside" aria-label="Flyer inside spread">
  <div class="abs band concrete" role="img" aria-label="Photo of grooved concrete texture">
    <h2><span class="lead">We Offers</span> <span class="strong">4 Different</span> <span class="light">Grooving Options</span></h2>
    <svg class="abs" style="left:350px;top:44px" width="160" height="16" viewBox="0 0 160 16" aria-hidden="true"><path d="M2 14 Q80 -4 158 12" fill="none" stroke="var(--green)" stroke-width="4"/></svg>
  </div>

  <div class="abs tagbar"><p><span class="t1">No More Slippery</span><span class="t2">Slats And Concrete Floors</span></p></div>
  <div class="photo" style="left:97px;top:173px;width:284px;height:352px;background:linear-gradient(180deg,#b8c4cc,#8e9090 45%,#d9dbd8)" role="img" aria-label="Photo of a grooving machine spraying water over concrete"></div>

  <div class="abs deep">
    <h3 class="heading">Deep Grooving</h3>
    <ul>
      <li>Ideal For Safety &amp; Efficiency <em>Our Hugely Popular Deep Straight Line Grooving, Long Lasting, Minimal Hoof Wear.</em></li>
      <li>Create Safe And Secure Flooring, <em>Cows Walk Without Hesitation.</em></li>
      <li>Achieve Groove Spacing <em>For Optimal Hoof Function, Reduce Hoof Trauma.</em></li>
      <li>Ideal Grooves To New Concrete <em>Or Surfaces With Little To No Pattern Or Previous Grooving.</em></li>
      <li>Ideal Groove Pattern <em>As Promoted By The Pasturewide Programme.</em></li>
    </ul>
  </div>

  <div class="photo barn-yellow" style="left:0;top:535px;width:181px;height:135px" role="img" aria-label="Photo of a shed floor in warm light"></div>
  <div class="photo concrete" style="left:190px;top:535px;width:191px;height:135px" role="img" aria-label="Photo of grooving work in progress"></div>
  <div class="photo concrete" style="left:389px;top:535px;width:191px;height:135px" role="img" aria-label="Photo of radiating grooves on a shed floor"></div>

  <div class="photo mini-bg concrete-warm" role="img" aria-label="Photo of grooved slats in a cattle shed"></div>
  <div class="abs mini-green"></div>
  <div class="abs mini-box">
    <div class="photo concrete-warm" style="left:20px;top:22px;width:105px;height:218px" role="img" aria-label="Photo of a long mini-grooved passageway"></div>
    <div class="photo concrete-warm" style="left:130px;top:22px;width:104px;height:218px" role="img" aria-label="Close-up photo of mini grooves on slats"></div>
    <h3 class="heading">Mini Grooving</h3>
    <p class="p1">Smaller Dimensions Ideal Option For Heifer Housing And High Activity Areas Such As Parlours And Handling Areas</p>
    <p class="p2">An Ideal Solution For Regaining Traction On Old Previous Grooving That Has Lost Its Traction Without Loosing Stability</p>
  </div>
</section>

</body>
</html>
```